Tessaro Lane Website

We are starting a marketing company and to do that we need a website! We want a website that will inspire and persuade to bring out the awesomeness in our clients.
What we want to see:
- Inspirational and persuasive imagery that relate to Branding.
- No cliche images eg. business man, suits and hand shakes
- We want to transform and educate our clients.
- We want to show them the path and would like our website to really act as a guide that guides them step by step through our process.
- We want the portray that we are an investment but not have a pretentious way to it. We put our heart into every project and that is how we treat our clients.
-When you submit your design please include what platform you have created for. Preference would be Wordpress or Joobla.

We have included the psd file for the wire frame, logo files, font files, site map and a link to a video we create to give you more information on what we would like to see. http://clipvault-demo.example/t/qx903LmaP

Feel free to make small modification to the logos if you think it will improve it. Your creativity and advice is most welcome.

One thing we forgot. We would like to have our contact information near the top of the website as well as at the bottom.  Here is out contact info:

Email: info@tessarolane.ca
Phone: 555-013-4829

Reason: As we are new with the platform and that we want to optimize our results, we decided to extend the deadline by 15 days. Thanks!

Target Market(s)

28-60, Male and Female, Oil field, Local Businesses, Dentists, Chiropractors, Hair salon, Construction/Renovation, Events etc

Industry/Entity Type

Investment

Requirements
Must have
• - 4 Inspirational and persuasive Imagery for the top portion of the website
- Must have a feel as if your not on a website an example of this is linked below.
http://www.pitchgallery-demo.example/design/482907/web-design-by-dalia-fenwick
Nice to have
• - Creative advice from you.
- Creative buttons for Get Free Quote and Subscribe buttons. Something out of the box that draws peoples attention. eg. a 'B' button. Just and example but still something related to branding.
Should not have
• No Cliches

```html
<!DOCTYPE html>
<html lang="en">
<head>
<meta charset="utf-8">
<title>Tessaro Lane</title>
<link href="https://fonts.googleapis.com/css2?family=Open+Sans:wght@400;600;700&family=Signika:wght@600;700&display=swap" rel="stylesheet">
<style>
:root{
  --green:#5a9a1e;
  --green-light:#8cc63f;
  --green-dark:#3f7a12;
  --ink:#2b2b2b;
  --text:#5a5a5a;
  --grey-band:#8a8a80;
  --page:#f7f7f7;
  --panel:#e4e4e4;
  --hero-warm:#eadfcf;
  --white:#ffffff;
  --footer-top:#9a9a9a;
  --footer-bottom:#2e2e2e;
}
*{box-sizing:border-box;margin:0;padding:0}
html,body{width:1200px;height:1113px;overflow:hidden;background:var(--page)}
body{font-family:"Open Sans",Arial,sans-serif;color:var(--text);position:relative}
.abs{position:absolute}
.topbar{left:0;top:0;width:1200px;height:42px;background:linear-gradient(#6e6e64,#a9a99c 60%,#8f8f84);border-bottom:1px solid #cfcfc5}
.contact{display:flex;align-items:center;gap:6px;color:var(--white);font-size:17px;white-space:nowrap}
.contact b{font-weight:700}
.contact .sep{margin:0 3px}
.topbar .contact{position:absolute;right:19px;top:9px}
.hero{left:0;top:43px;width:1200px;height:379px;background:linear-gradient(180deg,#fbfaf8 0%,var(--hero-warm) 100%)}
.sidepanel{left:118px;top:43px;width:230px;height:379px;background:linear-gradient(90deg,rgba(220,220,220,.85),rgba(240,240,240,.6))}
.brand{left:134px;top:62px;display:flex;align-items:center;gap:8px}
.brand-dot{width:14px;height:14px;border-radius:50%;background:var(--green)}
.brand-name{font-family:"Signika",Arial,sans-serif;font-weight:700;font-size:27px;color:var(--green);letter-spacing:.5px;line-height:1}
.tagline{left:161px;top:119px;font-size:13px;font-style:italic;color:#333}
.mainnav{left:135px;top:166px;list-style:none}
.mainnav li{font-weight:600;font-size:15.5px;color:var(--ink);height:37.5px;letter-spacing:.3px}
.hero-art{left:348px;top:43px;width:632px;height:379px;background:radial-gradient(circle at 72% 68%,#f2d3b8 0%,#e9f3e0 32%,#7fc64a 34%,#3f9a15 38%,rgba(255,255,255,0) 40%),linear-gradient(135deg,#ffffff 0%,#e6e6e6 45%,#eadfcf 100%)}
.steps{right:27px;top:113px;list-style:none;text-align:right}
.steps li{display:flex;justify-content:flex-end;align-items:center;gap:7px;height:69px;font-family:"Signika",Arial,sans-serif;font-weight:700;font-size:17px;color:var(--ink)}
.steps li.active{color:var(--green)}
.steps .dot{width:16px;height:16px;border-radius:50%;background:radial-gradient(circle at 35% 35%,#d8d8d8,#777)}
.steps li.active .dot{background:radial-gradient(circle at 35% 35%,#c8ef8a,#5fa521)}
.card{background:repeating-linear-gradient(45deg,#e2e2e2 0 2px,#e8e8e8 2px 4px);box-shadow:0 12px 10px -8px rgba(0,0,0,.25)}
.social{left:120px;top:447px;width:228px;height:93px}
.social h3{position:absolute;left:22px;top:17px;font-family:"Signika",Arial,sans-serif;font-weight:700;font-size:21px;color:#555}
.social-icons{position:absolute;left:24px;top:47px;display:flex;gap:8px}
.social-icons span{width:31px;height:31px;border-radius:3px;background:#8a8a8a;border:1px solid #666}
.newsletter{left:361px;top:447px;width:711px;height:93px}
.newsletter h3{position:absolute;left:0;width:100%;top:10px;text-align:center;font-family:"Open Sans",Arial,sans-serif;font-weight:700;font-size:23px;color:#666}
.newsletter h3 em{font-style:normal;color:var(--green)}
.email-field{position:absolute;left:54px;top:46px;width:521px;height:38px;background:var(--white);border:1px solid #bbb;border-radius:3px;font-size:14px;color:#666;padding:9px 9px}
.subscribe{position:absolute;left:557px;top:46px;width:102px;height:38px;border-radius:3px;background:linear-gradient(#bdbdbd,#8c8c8c);color:var(--white);font-weight:700;font-size:16px;text-align:center;line-height:38px}
.welcome{left:122px;top:580px;font-family:"Signika",Arial,sans-serif;font-weight:700;font-size:25px;color:var(--ink);letter-spacing:.3px}
.mission-title{left:125px;top:624px;font-weight:700;font-size:15.5px;color:var(--green)}
.copy{left:125px;width:940px;font-size:15.5px;line-height:21px;color:var(--text)}
.mission-copy{top:645px}
.benefits{left:126px;top:718px;list-style:none}
.benefits li{display:flex;align-items:center;gap:11px;height:34.5px;font-size:15.5px;color:var(--ink)}
.tick{width:19px;height:19px;border-radius:3px;background:var(--green-light);display:flex;align-items:center;justify-content:center}
.closing-copy{top:907px}
.quote-btn{left:919px;top:831px;width:157px;height:40px;border-radius:3px;background:linear-gradient(#6fb32c,var(--green-dark));border:1px solid #3b6e12;color:var(--white);font-weight:700;font-size:16px;text-align:center;line-height:38px}
.footer{left:0;top:994px;width:1200px;height:119px;background:linear-gradient(var(--footer-top),var(--footer-bottom))}
.footnav{position:absolute;left:123px;top:31px;display:flex;gap:14px;list-style:none;font-weight:600;font-size:17px;color:var(--white)}
.copyright{position:absolute;left:123px;top:59px;font-size:16.5px;color:var(--green-light)}
.footer .contact{position:absolute;right:124px;top:33px}
</style>
</head>
<body>
<header>
  <div class="abs topbar">
    <div class="contact">
      <svg width="16" height="12" viewBox="0 0 16 12" aria-hidden="true"><rect width="16" height="12" fill="#222"/><path d="M0 0l8 7 8-7" fill="none" stroke="#aaa" stroke-width="1.4"/></svg>
      <span>info@tessarolane.ca</span><span class="sep">|</span>
      <svg width="13" height="13" viewBox="0 0 24 24" aria-hidden="true"><path fill="#222" d="M6.6 10.8a15 15 0 006.6 6.6l2.2-2.2a1 1 0 011-.25 11.4 11.4 0 003.6.57 1 1 0 011 1V20a1 1 0 01-1 1A17 17 0 013 4a1 1 0 011-1h3.5a1 1 0 011 1c0 1.25.2 2.45.57 3.6a1 1 0 01-.25 1z"/></svg>
      <b>555-013-4829</b>
    </div>
  </div>
  <div class="abs hero"></div>
  <div class="abs hero-art" role="img" aria-label="Green check mark ticking a row of boxes beside a green seal framing raised thumbs-up hands"></div>
  <div class="abs sidepanel"></div>
  <div class="abs brand"><span class="brand-dot"></span><span class="brand-name">TESSARO LANE</span></div>
  <div class="abs tagline">Because You're Awesome!</div>
  <ul class="abs mainnav">
    <li>STRATEGY</li><li>PORTFOLIO</li><li>ABOUT US</li><li>CONTACT US</li><li>BLOG</li>
  </ul>
  <ul class="abs steps">
    <li class="active">TESSARO LANE <span class="dot"></span></li>
    <li>BE FOUND <span class="dot"></span></li>
    <li>CONNECT <span class="dot"></span></li>
    <li>GET GROWING <span class="dot"></span></li>
  </ul>
</header>

<main>
  <section class="abs card social">
    <h3>CONNECT WITH US</h3>
    <div class="social-icons">
      <span aria-label="Social profile"></span><span aria-label="Social profile"></span><span aria-label="Social profile"></span><span aria-label="News feed"></span><span aria-label="Video channel"></span>
    </div>
  </section>
  <section class="abs card newsletter">
    <h3><em>GET TIPS AND TRICKS!</em> SUBSCRIBE TO OUR NEWSLETTER</h3>
    <div class="email-field">your email id</div>
    <div class="subscribe">Subscribe</div>
  </section>

  <h1 class="abs welcome">WELCOME TO TESSARO LANE</h1>
  <h2 class="abs mission-title">Our Mission</h2>
  <p class="abs copy mission-copy">Etiam adipiscing mollis nulla, ac bibendum elit commodo ac. Pellentesque vehicula sodales vulputate. Suspendisse vel semper tortor. Duis tristique pharetra ligula sed bibendum. Etiam adipiscing mollis nulla, ac bibendum elit commodo ac. Etiam adipiscing mollis nulla, ac bibendum elit commodo ac.</p>
  <ul class="abs benefits">
    <li><span class="tick"><svg width="12" height="10" viewBox="0 0 12 10" aria-hidden="true"><path d="M1.5 5l3 3 6-6.5" fill="none" stroke="#fff" stroke-width="2.2"/></svg></span>Nam ac risus metus, sit amet blandit ante.</li>
    <li><span class="tick"><svg width="12" height="10" viewBox="0 0 12 10" aria-hidden="true"><path d="M1.5 5l3 3 6-6.5" fill="none" stroke="#fff" stroke-width="2.2"/></svg></span>Nunc adipiscing, ipsum eu scelerisque euismod, diam nisl condimentum neque,</li>
    <li><span class="tick"><svg width="12" height="10" viewBox="0 0 12 10" aria-hidden="true"><path d="M1.5 5l3 3 6-6.5" fill="none" stroke="#fff" stroke-width="2.2"/></svg></span>Vel gravida ligula velit vitae nisl. Pellentesque at dignissim ipsum. Vivamus id massa arcu.</li>
    <li><span class="tick"><svg width="12" height="10" viewBox="0 0 12 10" aria-hidden="true"><path d="M1.5 5l3 3 6-6.5" fill="none" stroke="#fff" stroke-width="2.2"/></svg></span>Phasellus feugiat condimentum neque ac bibendum.</li>
    <li><span class="tick"><svg width="12" height="10" viewBox="0 0 12 10" aria-hidden="true"><path d="M1.5 5l3 3 6-6.5" fill="none" stroke="#fff" stroke-width="2.2"/></svg></span>Pellentesque dictum lectus sapien, eu pulvinar eros.</li>
  </ul>
  <div class="abs quote-btn">Get a Free Quote!</div>
  <p class="abs copy closing-copy">Maecenas lacinia, nulla at interdum dapibus, velit sapien posuere eros, et hendrerit purus erat quis est. Proin commodo blandit mauris sed convallis. Donec tellus metus, feugiat sed condimentum congue, dignissim ut leo.</p>
</main>

<footer class="abs footer">
  <ul class="footnav">
    <li>Site Map</li><li>Strategy</li><li>Portfolio</li><li>About Us</li><li>Contact Us</li><li>Blog</li>
  </ul>
  <div class="copyright">©TESSARO LANE INC. 2013</div>
  <div class="contact">
    <svg width="16" height="12" viewBox="0 0 16 12" aria-hidden="true"><rect width="16" height="12" fill="#111"/><path d="M0 0l8 7 8-7" fill="none" stroke="#999" stroke-width="1.4"/></svg>
    <span>info@tessarolane.ca</span><span class="sep">|</span>
    <svg width="13" height="13" viewBox="0 0 24 24" aria-hidden="true"><path fill="#111" d="M6.6 10.8a15 15 0 006.6 6.6l2.2-2.2a1 1 0 011-.25 11.4 11.4 0 003.6.57 1 1 0 011 1V20a1 1 0 01-1 1A17 17 0 013 4a1 1 0 011-1h3.5a1 1 0 011 1c0 1.25.2 2.45.57 3.6a1 1 0 01-.25 1z"/></svg>
    <b>555-013-4829</b>
  </div>
</footer>
</body>
</html>
```